business cards, stationary
lets see what you got
Use specific fonts
up to designer
Modern
Calvin Marsh
Director of Sales
1870 Quarrymill road, Suite 114 Burlington, On L4K 3P8
Calvin@sunlanejourneys.example
www.sunlanejourneys.example
BBM: 58720936
LOGO on back

```html
<!DOCTYPE html>
<html lang="en">
<head>
<meta charset="utf-8">
<title>Sun Lane Journeys business cards</title>
<link href="https://fonts.googleapis.com/css2?family=Ubuntu:wght@400;500;700&display=swap" rel="stylesheet">
<style>
  :root{
    --purple:#4a2a7c;
    --green:#8cc63f;
    --white:#ffffff;
    --stage:#8b5e3c;
    --ink-soft:#e6def2;
    --rule:rgba(255,255,255,.4);
  }
  *{box-sizing:border-box;margin:0;padding:0}
  html,body{width:1200px;height:901px;overflow:hidden}
  body{background:var(--stage);font-family:"Ubuntu",sans-serif;position:relative}

  .card{position:absolute;width:487px;height:272px;border-radius:14px;overflow:hidden;
        box-shadow:0 4px 10px rgba(0,0,0,.25)}
  .card--front{left:100px;top:124px;background:var(--white)}
  .card--back-purple{left:611px;top:124px;background:var(--purple)}
  .card--back-white{left:100px;top:438px;background:var(--white)}
  .card--back-green{left:611px;top:438px;background:var(--green)}

  .brand{position:absolute;left:0;right:0;display:flex;flex-direction:column;align-items:center;gap:10px}
  .brand__dot{width:44px;height:44px;border-radius:50%;background:var(--green)}
  .brand__name{font-weight:700;font-size:31px;letter-spacing:-.5px;line-height:34px;color:var(--purple)}
  .card--back-purple .brand__name,.card--back-green .brand__name{color:var(--white)}
  .card--back-green .brand__dot{background:var(--white)}
  .card--front .brand{top:22px}
  .card--back-purple .brand,.card--back-white .brand,.card--back-green .brand{top:84px}

  .front__wave{position:absolute;left:0;bottom:0;width:487px;height:160px}

  .contact{position:absolute;left:0;right:0;top:182px;height:50px;color:var(--white);font-size:9.5px;line-height:13px}
  .contact__person{position:absolute;left:24px;top:2px;padding-right:14px;border-right:1px solid var(--rule)}
  .contact__name{font-size:17px;line-height:20px;font-weight:400}
  .contact__role{color:var(--ink-soft)}
  .contact__address{position:absolute;left:170px;top:0;width:132px}
  .contact__lines{position:absolute;left:308px;top:0;list-style:none}
  .contact__lines li{display:flex;align-items:center;gap:6px;white-space:nowrap}
  .contact__lines svg{width:8px;height:8px;fill:var(--white);flex:none}

  .front__rule{position:absolute;left:18px;right:18px;bottom:26px;height:1px;background:var(--rule)}
  .contact__web{position:absolute;left:0;right:0;bottom:10px;text-align:center;color:var(--white);font-size:8.5px;line-height:11px;letter-spacing:.3px}
</style>
</head>
<body>
  <section class="card card--front">
    <div class="brand">
      <span class="brand__dot"></span>
      <span class="brand__name">sunlanejourneys</span>
    </div>
    <svg class="front__wave" viewBox="0 0 487 160" preserveAspectRatio="none" aria-hidden="true">
      <path d="M0 40 C120 10 260 60 487 20 L487 160 L0 160 Z" fill="var(--green)"/>
      <path d="M0 52 C140 24 280 74 487 34 L487 160 L0 160 Z" fill="var(--purple)"/>
    </svg>
    <div class="contact">
      <div class="contact__person">
        <p class="contact__name">Calvin Marsh</p>
        <p class="contact__role">Director of Sales</p>
      </div>
      <p class="contact__address">1870 Quarrymill road,<br>Suite 114<br>Alderbrook, On L4K 3P8</p>
      <ul class="contact__lines">
        <li><svg viewBox="0 0 8 8"><rect x="1.5" y="0" width="5" height="8" rx="1"/></svg>1.800.555.0142</li>
        <li><svg viewBox="0 0 8 8"><circle cx="4" cy="4" r="3.5"/></svg>905.555.0187</li>
        <li><svg viewBox="0 0 8 8"><rect x="0" y="1" width="8" height="6" rx="1"/></svg>Calvin@sunlanejourneys.example</li>
        <li><svg viewBox="0 0 8 8"><path d="M0 0 H8 V6 H3 L1 8 V6 H0 Z"/></svg>BBM: 58720936</li>
      </ul>
    </div>
    <span class="front__rule"></span>
    <p class="contact__web">www.sunlanejourneys.example</p>
  </section>

  <section class="card card--back-purple">
    <div class="brand"><span class="brand__dot"></span><span class="brand__name">sunlanejourneys</span></div>
  </section>

  <section class="card card--back-white">
    <div class="brand"><span class="brand__dot"></span><span class="brand__name">sunlanejourneys</span></div>
  </section>

  <section class="card card--back-green">
    <div class="brand"><span class="brand__dot"></span><span class="brand__name">sunlanejourneys</span></div>
  </section>
</body>
</html>
```